依頼詳細
開催日の数日前に、会場周辺ご近所のポストへチラシを投函しています。枚数は毎回10,000枚前後です。そのチラシのデザイン作成をお願い致します。ポストに入っていたチラシを見て、思わす「ん?面白そうだから気軽に一度何か持って行ってみようかな」と思ってもらえるような、あと来場される方は中高年からご年配の方がほとんどなので、安心感を与えるデザインを希望です。
記載項目

```html
<!DOCTYPE html>
<html lang="ja">
<head>
<meta charset="utf-8">
<title>無料査定会 チラシ</title>
<link href="https://fonts.googleapis.com/css2?family=Noto+Sans+JP:wght@400;700;900&family=Noto+Serif+JP:wght@700;900&display=swap" rel="stylesheet">
<style>
:root{
  --navy:#1d2a4a;
  --ink:#1a1a1a;
  --red:#d0121b;
  --gold1:#b88a2e;
  --gold2:#e3c36d;
  --band:#e8edf4;
  --line:#9aa6b8;
  --white:#ffffff;
}
*{margin:0;padding:0;box-sizing:border-box}
html,body{width:848px;height:1200px;overflow:hidden;background:var(--white)}
body{font-family:"Noto Sans JP",sans-serif;color:var(--ink);position:relative}
.hero{position:absolute;left:0;top:0;width:848px;height:345px;
  background:linear-gradient(160deg,#f4f1ec 0%,#e4ded3 55%,#cfc7b9 100%)}
.band{position:absolute;left:0;top:345px;width:848px;height:800px;background:var(--band)}
.note-badge{position:absolute;left:728px;top:300px;width:110px;height:110px;border-radius:50%;
  background:var(--navy);color:var(--white);font-size:13px;font-weight:700;line-height:1.45;
  display:flex;align-items:center;justify-content:center;text-align:center;border:3px solid var(--white)}
.question{position:absolute;top:420px;width:100%;text-align:center;font-size:30px;font-weight:900;color:var(--navy)}
.items{position:absolute;left:22px;top:478px;width:804px;display:flex;gap:8px}
.item{flex:1;height:66px;background:linear-gradient(180deg,var(--gold2),var(--gold1));color:var(--white);
  font-size:16px;font-weight:700;line-height:1.3;display:flex;align-items:center;justify-content:center;text-align:center;border-radius:3px}
.lead{position:absolute;top:566px;left:0;width:100%;text-align:center;font-size:26px;font-weight:900;color:var(--red)}
.title{position:absolute;top:598px;left:30px;width:650px;text-align:center;font-family:"Noto Serif JP",serif;font-weight:900;font-size:112px;letter-spacing:6px;line-height:1.1}
.limit{position:absolute;left:690px;top:600px;width:130px;height:130px;border-radius:50%;background:var(--red);color:var(--white);
  display:flex;flex-direction:column;align-items:center;justify-content:center;font-weight:900;font-size:28px;line-height:1.2}
.limit small{font-size:17px;font-weight:700}
.venue{position:absolute;top:740px;left:0;width:100%;text-align:center;font-size:36px;font-weight:900;white-space:nowrap;line-height:1.3}
.venue .br{color:var(--red)}
.map{position:absolute;left:30px;top:812px;width:400px;height:310px;background:#c9ccd2;display:flex;align-items:center;justify-content:center;font-size:20px;color:#333}
.info{position:absolute;left:448px;top:812px;width:372px}
.row{display:flex;align-items:center;gap:8px;margin-bottom:6px;white-space:nowrap}
.label{background:var(--navy);color:var(--white);font-size:14px;font-weight:700;padding:4px 0;line-height:1.2;width:54px;text-align:center;flex:none}
.value{font-family:"Noto Serif JP",serif;font-weight:900;font-size:29px;color:var(--red);line-height:1.3}
.value small{font-size:17px;color:var(--ink)}
.history{margin-top:8px;background:var(--ink);color:var(--white);font-size:20px;font-weight:700;text-align:center;padding:3px 0}
.brand{margin-top:6px;font-size:38px;font-weight:700;color:var(--ink);letter-spacing:2px;line-height:1.15;white-space:nowrap}
.addr-small{font-size:10px;color:#444}
.phone{display:flex;align-items:center;gap:8px;margin-top:4px}
.phone-num{font-size:36px;font-weight:900;color:var(--ink);line-height:1.2}
.company{margin-top:6px;display:flex;gap:10px;align-items:flex-start;border-top:1px solid var(--line);padding-top:6px}
.company-name{font-size:18px;font-weight:700;white-space:nowrap}
.company-addr{font-size:10px;line-height:1.5;color:#333}
</style>
</head>
<body>
<div class="hero" role="img" aria-label="虫眼鏡越しに見るリビングルームの線画イラスト"></div>
<div class="band"></div>
<div class="note-badge">古いデザインや<br>過去の収集品など<br>なんでもOK!</div>

<p class="question">ご自宅にお宝は眠っていませんか？</p>
<div class="items">
  <div class="item">金・プラチナなどの<br>貴金属</div>
  <div class="item">ダイヤ・ルビー・<br>サファイヤなど</div>
  <div class="item">古銭・記念コイン</div>
  <div class="item">時計・ブランド品<br>一点からOK</div>
  <div class="item">絵画・掛軸・<br>陶磁器 など</div>
</div>

<p class="lead">まずはご参加ください！</p>
<h1 class="title">無料査定会</h1>
<div class="limit">2日間<br>限定<small>（年1回）</small></div>
<p class="venue"><span class="br">［</span>○○○○○○○○○○○○○○<span class="br">］</span>にて開催！</p>

<div class="map" role="img" aria-label="会場周辺の地図">地図</div>

<div class="info">
  <div class="row"><span class="label">開催日</span><span class="value">00月00日<small>(土)</small>・00日<small>(日)</small></span></div>
  <div class="row"><span class="label">時 間</span><span class="value">00:00〜00:00</span></div>
  <div class="history">創業12年の実績</div>
  <div class="brand">SILVER CROWN</div>
  <div class="addr-small">査定のご相談はお気軽に</div>
  <div class="phone">
    <svg width="40" height="30" viewBox="0 0 44 32" aria-hidden="true">
      <rect x="1" y="1" width="42" height="30" rx="6" fill="none" stroke="#1a1a1a" stroke-width="2"/>
      <path d="M14 9c-2 2 0 7 4 11s9 6 11 4l2-2-4-4-3 2c-2-1-5-4-6-6l2-3-4-4z" fill="#1a1a1a"/>
    </svg>
    <span class="phone-num">0120-00-4321</span>
  </div>
  <div class="company">
    <span class="company-name">株式会社 ミナト</span>
    <span class="company-addr">〒000-0000 東京都○○区○○町0-0-0<br>【電話受付時間】平日 00:00〜00:00<br>TEL 00-0000-0000</span>
  </div>
</div>
</body>
</html>
```